Business Card Design

I need a business card for my rental business. The business is named:
Hire a Vorlatrike Brenmoor
www.hireavorlatrikebrenmoor.example
(555) 014-2937
This will be a business card that I will leave at other businesses as advertisement so it needs to have the name, website, and phone number.
Please feel free to be creative. This is a new business so I have no designs.
Thank you very much for your time and I look forward to receiving your designs
Target Market(s)
Local rental customers
Industry/Entity Type
Business
Contact Information for Business Card
Please check out my website:
Other font styles liked:
- anything creative
Colors
Designer to choose colors to be used in the design.
Requirements
Must have
- Business name, phone, website. Rentals available hourly or daily. Book online

```html
<!DOCTYPE html>
<html lang="en">
<head>
<meta charset="utf-8">
<title>Hire a Vorlatrike Brenmoor – Business Card</title>
<link href="https://fonts.googleapis.com/css2?family=Audiowide&family=Open+Sans:wght@400;600&display=swap" rel="stylesheet">
<style>
  :root {
    --bg: #3a4450;
    --card-dark: #0b0b0b;
    --card-light: #fbfbfa;
    --accent: #f08a1e;
    --ornament-dark: #3a3735;
    --ornament-light: #d2d2d2;
    --text-light: #e6e6e6;
    --text-muted: #bdbdbd;
    --text-dark: #1a1a1a;
    --icon: #111111;
  }
  * { margin: 0; padding: 0; box-sizing: border-box; }
  html, body { width: 1200px; height: 1000px; overflow: hidden; }
  body { background: var(--bg); position: relative; font-family: "Open Sans", Arial, sans-serif; }

  .card { position: absolute; width: 620px; height: 354px; overflow: hidden; box-shadow: 0 10px 24px rgba(0,0,0,.35); }

  /* Front */
  .card--front { left: 90px; top: 110px; background: var(--card-dark); }
  .card--front .ornament { position: absolute; right: 10px; top: -10px; width: 240px; height: 240px; border-radius: 50%;
    background: radial-gradient(circle, var(--card-dark) 0 34%, var(--ornament-dark) 36% 70%, rgba(58,55,53,0) 72%); }
  .brand-name { font-family: "Audiowide", "Arial Black", sans-serif; text-transform: uppercase; letter-spacing: .5px; font-weight: 400; position: relative; }
  .card--front .brand-name { position: absolute; left: 30px; top: 108px; font-size: 22px; color: var(--accent); }
  .card--front .web { position: absolute; left: 40px; top: 140px; font-size: 17px; font-weight: 600; color: var(--text-light); }
  .offer-list { position: absolute; left: 300px; top: 174px; list-style: none; color: var(--text-muted); font-size: 18px; line-height: 26px; }
  .offer-list li::before { content: ""; display: inline-block; width: 8px; height: 8px; border-radius: 50%; background: var(--text-muted); margin-right: 8px; vertical-align: middle; }
  .vehicle-photo { position: absolute; left: 40px; top: 238px; width: 340px; height: 116px; border-radius: 50px 110px 10px 10px; background: linear-gradient(100deg, #1c1c1c 0%, #d9731a 45%, #222 70%, #e6801f 100%); }

  /* Back */
  .card--back { left: 490px; top: 520px; background: var(--card-light); }
  .card--back .ornament { position: absolute; right: 40px; top: -20px; width: 240px; height: 240px; border-radius: 50%;
    background: radial-gradient(circle, var(--card-light) 0 34%, var(--ornament-light) 36% 70%, rgba(210,210,210,0) 72%); }
  .vehicle-photo--faded { position: absolute; right: 50px; top: 80px; width: 160px; height: 200px; border-radius: 40px; background: linear-gradient(160deg, #d6d6d6, #9fc6d8 60%, #cfcfcf); opacity: .5; }
  .card--back .brand-name { position: absolute; left: 40px; top: 100px; font-size: 21px; color: var(--text-dark); }
  .person { position: absolute; right: 70px; top: 132px; text-align: center; }
  .person-name { font-size: 22px; font-weight: 600; color: #333; border-bottom: 2px solid #333; padding: 0 6px; }
  .person-role { font-size: 12px; font-weight: 600; color: #333; margin-top: 2px; }
  .contact-list { position: absolute; left: 40px; top: 170px; list-style: none; font-size: 14px; color: var(--text-dark); }
  .contact-list li { display: flex; align-items: center; height: 30px; gap: 8px; }
  .contact-list svg { width: 22px; height: 22px; flex: none; }
  .card--back .web { position: absolute; right: 40px; bottom: 26px; font-size: 14px; font-weight: 600; color: var(--text-dark); }
</style>
</head>
<body>

<section class="card card--front">
  <div class="ornament" role="img" aria-label="Decorative segmented ring ornament"></div>
  <h1 class="brand-name">Hire a Vorlatrike Brenmoor</h1>
  <p class="web">www.hireavorlatrikebrenmoor.example</p>
  <ul class="offer-list">
    <li>Rentals available hourly or daily</li>
    <li>Book online</li>
  </ul>
  <div class="vehicle-photo" role="img" aria-label="Photo of a black and orange three-wheeled roadster"></div>
</section>

<section class="card card--back">
  <div class="ornament" role="img" aria-label="Decorative segmented ring ornament"></div>
  <div class="vehicle-photo--faded" role="img" aria-label="Faded photo of a blue three-wheeled roadster"></div>
  <h2 class="brand-name">Hire a Vorlatrike Brenmoor</h2>
  <div class="person">
    <p class="person-name">Dorian</p>
    <p class="person-role">Director</p>
  </div>
  <ul class="contact-list">
    <li>
      <svg viewBox="0 0 24 24" aria-hidden="true"><circle cx="12" cy="12" r="12" fill="var(--icon)"/><path d="M12 5a4.5 4.5 0 0 0-4.5 4.5C7.5 13 12 19 12 19s4.5-6 4.5-9.5A4.5 4.5 0 0 0 12 5zm0 6.3a1.8 1.8 0 1 1 0-3.6 1.8 1.8 0 0 1 0 3.6z" fill="#fff"/></svg>
      Route 418, Brenmoor, Texas 70000
    </li>
    <li>
      <svg viewBox="0 0 24 24" aria-hidden="true"><circle cx="12" cy="12" r="12" fill="var(--icon)"/><path d="M8.5 6.5l2 2.5-1.2 1.5a8 8 0 0 0 4.2 4.2l1.5-1.2 2.5 2-1.3 2c-4.6-.3-8.7-4.4-9-9z" fill="#fff"/></svg>
      (555) 014-2937
    </li>
    <li>
      <svg viewBox="0 0 24 24" aria-hidden="true"><circle cx="12" cy="12" r="12" fill="var(--icon)"/><rect x="8" y="5" width="8" height="14" rx="1.5" fill="#fff"/><rect x="9.3" y="7" width="5.4" height="9" fill="var(--icon)"/></svg>
      555 019 4460
    </li>
    <li>
      <svg viewBox="0 0 24 24" aria-hidden="true"><circle cx="12" cy="12" r="12" fill="var(--icon)"/><rect x="6" y="8" width="12" height="8" fill="#fff"/><path d="M6 8l6 5 6-5" fill="none" stroke="var(--icon)" stroke-width="1.2"/></svg>
      mail@hireavorlatrikebrenmoor.example
    </li>
  </ul>
  <p class="web">www.hireavorlatrikebrenmoor.example</p>
</section>

</body>
</html>
```